Packaging for a gift bag make your own dog biscuits.

I am looking for someone who can design me a card design that can be attached to a gift bag containing all the ingredients someone would need in order to make their own dog biscuits. The dog buscuits will be chocolate bone shaped biscuits. My company name is Maple Fern Pantry and i have attached a copy of the company logo to this description. I would like something classy and artisan but not too child like. The design i am looking for is purely the design that will capture the customer all the leagl informastion will be at the back to there is no need to worry about any of this at this stage. The design would need to fit a rectangular or similar shaped piece of card no bigger than 9cm - 14cm I have also attached some pictures of a similar product to give you an idea. The gift bags they will be attached to will be 11cm x 16cm.
The gift bags will be red so it would be nice for the design to compliment this. Ok so just to add a slight complication I am now considering a tent carton as an alternative. I have a picture to a similar type product below. The box I have here is 19cm high (11cm been the square before the tent) 9.5cm width and 7cm girth.

Target Market(s)

Dog lovers, people who visit artisan markets and like to spend time with their much loved fur family.

Font styles to use
Decorative

Colors

Designer to choose colors to be used in the design.

Requirements
Must have
• A classy but artisan design that will attract both adults and kids and may also be something that could be purchased as a gift.
Nice to have
• Something to compliment the red gift bag. The logo visible somewhere on the design and the design in keeping with the company logo.
Should not have
• Any familiar cartoon characters, or a child like feel

```html
<!DOCTYPE html>
<html lang="en">
<head>
<meta charset="utf-8">
<title>Maple Fern Pantry – Cookie Mix Gift Card</title>
<link href="https://fonts.googleapis.com/css2?family=Mulish:wght@600;700;800&display=swap" rel="stylesheet">
<style>
  :root {
    --backdrop: #e31529;
    --tan-band: #b9905f;
    --check-band: #a47a50;
    --gingham-band: #d9c097;
    --stripe-dark: #5a3a20;
    --frame-white: #ffffff;
    --brand-brown: #8a4a17;
    --label-tan: #b07a4c;
    --body-grey: #4a4038;
    --art-brown: #8b5a34;
    --art-cream: #e9d6bd;
    --ribbon-red: #d0141e;
  }
  html, body {
    margin: 0;
    width: 1200px;
    height: 926px;
    overflow: hidden;
    background: var(--backdrop);
  }
  .canvas {
    position: relative;
    width: 1200px;
    height: 926px;
  }
  .gift-card {
    position: absolute;
    left: 360px;
    top: 70px;
    width: 480px;
    height: 780px;
    box-shadow: 0 18px 40px rgba(80, 0, 0, 0.35);
    font-family: "Mulish", sans-serif;
  }
  .gift-card svg.card-base {
    position: absolute;
    inset: 0;
  }
  .ribbon-art {
    position: absolute;
    left: 170px;
    top: -40px;
    width: 140px;
    height: 80px;
    border-radius: 40px;
    background: radial-gradient(ellipse at center, #e8323a 0%, var(--ribbon-red) 70%);
  }
  .mascot-art {
    position: absolute;
    left: 150px;
    top: 120px;
    width: 180px;
    height: 230px;
    border-radius: 50% 50% 40% 40%;
    background: radial-gradient(ellipse at 50% 40%, var(--art-cream) 0%, var(--art-brown) 75%);
  }
  .card-copy {
    position: absolute;
    left: 0;
    right: 0;
    text-align: center;
    margin: 0;
  }
  .brand-title {
    top: 378px;
    font-size: 44px;
    font-weight: 700;
    color: var(--brand-brown);
    letter-spacing: 0.5px;
  }
  .product-name {
    top: 460px;
    font-size: 30px;
    font-weight: 800;
    color: var(--label-tan);
    letter-spacing: 1px;
  }
  .product-blurb {
    top: 520px;
    left: 100px;
    right: 100px;
    font-size: 13px;
    font-weight: 700;
    line-height: 1.45;
    color: var(--body-grey);
    text-transform: uppercase;
    letter-spacing: 0.3px;
  }
  .net-weight {
    top: 590px;
    font-size: 17px;
    font-weight: 800;
    color: var(--brand-brown);
  }
  .brand-badge {
    position: absolute;
    left: 185px;
    top: 635px;
    width: 110px;
    height: 110px;
    border-radius: 50%;
    background: var(--frame-white);
    border: 3px solid var(--label-tan);
    box-sizing: border-box;
    display: flex;
    align-items: center;
    justify-content: center;
    text-align: center;
    font-size: 14px;
    font-weight: 800;
    line-height: 1.2;
    color: var(--brand-brown);
  }
</style>
</head>
<body>
<div class="canvas">
  <article class="gift-card">
    <svg class="card-base" width="480" height="780" viewBox="0 0 480 780" aria-hidden="true">
      <rect class="band-top" x="0" y="0" width="480" height="250" fill="var(--tan-band)"/>
      <rect class="band-check" x="0" y="250" width="480" height="400" fill="var(--check-band)"/>
      <rect class="band-gingham" x="0" y="650" width="480" height="130" fill="var(--gingham-band)"/>
      <rect x="0" y="244" width="480" height="12" fill="var(--stripe-dark)"/>
      <rect x="0" y="646" width="480" height="8" fill="var(--stripe-dark)"/>
      <path class="label-frame" fill="var(--frame-white)"
        d="M130 110
           C 170 110, 190 95, 240 95
           C 290 95, 310 110, 350 110
           C 395 110, 405 140, 410 180
           C 412 230, 445 240, 445 300
           C 445 360, 415 380, 415 430
           C 415 480, 448 500, 448 560
           C 448 620, 410 630, 410 680
           C 405 720, 380 730, 340 730
           C 300 730, 290 745, 240 745
           C 190 745, 180 730, 140 730
           C 100 730, 75 720, 70 680
           C 70 630, 32 620, 32 560
           C 32 500, 65 480, 65 430
           C 65 380, 35 360, 35 300
           C 35 240, 68 230, 70 180
           C 75 140, 85 110, 130 110 Z"/>
    </svg>
    <div class="ribbon-art" role="img" aria-label="Red satin ribbon bow tying the card"></div>
    <div class="mascot-art" role="img" aria-label="Illustration of a cheerful cartoon dog mascot wearing a shirt and tie"></div>
    <h1 class="card-copy brand-title">Maple Fern Pantry</h1>
    <h2 class="card-copy product-name">COOKIE MIX</h2>
    <p class="card-copy product-blurb">Lorem ipsum is simply dummy text of the printing and typesetting industry.</p>
    <p class="card-copy net-weight">NET WEIGHT 50G</p>
    <div class="brand-badge">Maple Fern<br>Pantry</div>
  </article>
</div>
</body>
</html>
```